Velmora Café retail envelop design

This is a single serve coffee product for the adventurer consumer. The product is Fair Trade, Organic coffee grounds in a single serve pouch that can be used as a quality pour over drip brew while on the go. We would like to use designs that show adventure/hiking/camping with earth tones that display a organic/biodegradable feel.The open width of envelope film is 200mmThe finished bag size is W 100mm * L 120mm. (Once sealed)The eye mark size is W 10* H 5 mm. (side seam)Top/Bottom heat seal: 8mmSide heat seal: 7mmPlease use the samples provided as a guide only. I would like to see what you can come up with. Please use our original logo attached.Three blend varieties: Brellowmark, Quillon, WarsawIG: @Velmoracafe
Updates

Target Market(s)

Adventurers, backpackers, campers, hikers, adventure riders, etc.

Colors

Designer to choose colors to be used in the design.

Requirements
Must have
• My Velmora Cafe logo, earthy feel (maybe black logo on earthy paper color backdrop?). Must show 12g size, instruction panel (this can be edited for visual appeal), IG account: Velmoracafe.
• Design will be printed in Matte finish.
Should not have
• It does not need all of the text that is shown on the back. I will prefer a more simplistic design rather than a crowded one.

```html
<!DOCTYPE html>
<html lang="en">
<head>
<meta charset="utf-8">
<title>Velmora Café – Tolvey single serve pouch</title>
<link rel="stylesheet" href="https://fonts.googleapis.com/css2?family=Oswald:wght@700&family=Amatic+SC:wght@700&family=Caveat:wght@500&display=swap">
<style>
  :root {
    --canvas: #ffffff;
    --paper: #f5cc9b;
    --paper-seal: #d9b184;
    --maroon: #773a39;
    --maroon-deep: #63302f;
    --flame: #9a4a55;
    --ink: #2e241c;
    --cream: #f2ece6;
    --gold: #d8b47e;
    --badge: #c9a57a;
  }
  * { margin: 0; padding: 0; box-sizing: border-box; }
  html, body { width: 1200px; height: 1200px; overflow: hidden; background: var(--canvas); }
  .canvas { position: relative; width: 1200px; height: 1200px; }
  .pouch { position: absolute; left: 150px; top: 105px; width: 900px; height: 990px; overflow: hidden; }
  .pouch-art { position: absolute; inset: 0; width: 100%; height: 100%; }
  .brand {
    position: absolute; left: 0; right: 0; top: 150px; text-align: center;
    font-family: "Oswald", sans-serif; font-weight: 700; color: var(--ink);
    font-size: 88px; line-height: 1.35; letter-spacing: 2px;
  }
  .brand-line { display: block; }
  .elevation {
    position: absolute; left: 248px; top: 640px;
    font-family: "Caveat", cursive; font-size: 24px; color: var(--gold);
  }
  .blend-name {
    position: absolute; left: 0; right: 0; top: 660px; text-align: center;
    font-family: "Amatic SC", sans-serif; font-weight: 700; font-size: 170px;
    line-height: 1; color: var(--cream); letter-spacing: 4px;
  }
  .origin {
    position: absolute; left: 0; right: 0; top: 846px; text-align: center;
    font-family: "Caveat", cursive; font-size: 32px; line-height: 40px; color: var(--gold);
  }
  .size-badge {
    position: absolute; left: 746px; top: 896px; width: 54px; height: 54px; border-radius: 50%;
    background: var(--badge); color: var(--maroon-deep);
    font-family: "Oswald", sans-serif; font-weight: 700; font-size: 22px;
    display: flex; align-items: center; justify-content: center;
  }
</style>
</head>
<body>
<main class="canvas">
  <section class="pouch">
    <svg class="pouch-art" viewBox="0 0 900 990">
      <defs>
        <radialGradient id="fireGlow" cx="50%" cy="50%" r="50%">
          <stop offset="0%" stop-color="var(--flame)" stop-opacity="0.95"/>
          <stop offset="100%" stop-color="var(--flame)" stop-opacity="0"/>
        </radialGradient>
      </defs>
      <rect class="paper-panel" x="0" y="0" width="900" height="990" fill="var(--paper)"/>
      <rect class="top-seal" x="0" y="0" width="900" height="30" fill="var(--paper-seal)"/>
      <path class="maroon-panel" d="M0 406 L450 530 L900 430 L900 990 L0 990 Z" fill="var(--maroon)"/>
      <rect class="bottom-seal" x="0" y="962" width="900" height="28" fill="var(--maroon-deep)"/>
      <ellipse class="campfire-centre" role="img" aria-label="Large campfire flame illustration behind the blend name"
               cx="450" cy="790" rx="200" ry="260" fill="url(#fireGlow)"/>
      <ellipse class="campfire-left" role="img" aria-label="Campfire with crossed logs illustration"
               cx="20" cy="720" rx="150" ry="160" fill="url(#fireGlow)"/>
      <ellipse class="campfire-right" role="img" aria-label="Campfire with crossed logs illustration"
               cx="880" cy="720" rx="150" ry="160" fill="url(#fireGlow)"/>
      <line class="rule" x1="235" y1="834" x2="680" y2="834" stroke="var(--gold)" stroke-width="2"/>
      <line class="rule" x1="235" y1="898" x2="740" y2="898" stroke="var(--gold)" stroke-width="2"/>
    </svg>
    <h1 class="brand"><span class="brand-line">VELMORA</span><span class="brand-line">CAFÉ</span></h1>
    <p class="elevation">Elevation 5344'</p>
    <h2 class="blend-name">TOLVEY</h2>
    <p class="origin">Mount Orrin &nbsp;|&nbsp; Brellowmark Park Fennick NY</p>
    <div class="size-badge">12G</div>
  </section>
</main>
</body>
</html>
```